Talent Management Company Needs Business Cards

Using one of the logos provided (attached) K&R Talent Collective needs a business card designed.
Please visit our website for more information about us-

www.krtalentcollective.example

The face should feature a dramatic presentation of the logo with the back being reserved for our professional information which is:

The information should be:
Dorian T. Vickers
C.E.O
Email: dtvickers@krtalentcollective.example
Mobile: 555-804-2917
Website: www.krtalentcollective.example

Marcus L. Vickers
Director of Public Relations
Email: mlvickers@krtalentcollective.example
Mobile: 555-806-3350

Jules R. Hampton
Director of Client Development
Email: jhampton@krtalentcollective.example

Simon Hurlock
Director of Brand Development
Email: shurlock@krtalentcollective.example

Would like the logo to have color. I would like to see one side red or black and the other side white but if it looks better in either black or red that would be fine to but would like to see how it comes out.

Please feel free to message me and if you would like just the icon alone I have other image files that I can send as well.

Target Market(s)

Professional Athletes, coaches, entertainers age 18-35 but also must be accepted in the business community

Industry/Entity Type

Business

Requirements
Must have
• 1) Use the logo
2) Double sided
3) Distinctive
Nice to have
• Small simple images for telephone, e-mail, and Url.

```html
<!DOCTYPE html>
<html lang="en">
<head>
<meta charset="utf-8">
<title>K&amp;R Talent Collective — Business Card</title>
<link href="https://fonts.googleapis.com/css2?family=Jost:wght@400;500;600&display=swap" rel="stylesheet">
<style>
  :root {
    --page: #e9e6e3;
    --ink: #0d0b0b;
    --ink-soft: #1c1a1a;
    --paper: #ffffff;
    --red: #e3202a;
    --light-text: #f4f4f4;
  }
  * { box-sizing: border-box; margin: 0; padding: 0; }
  html, body {
    width: 1200px; height: 1069px; overflow: hidden;
    background: var(--page);
    font-family: "Jost", sans-serif;
  }
  .sheet {
    position: relative; width: 1200px; height: 1069px;
    display: flex; flex-direction: column; align-items: center;
    justify-content: center; gap: 63px;
  }
  .card {
    position: relative; width: 770px; height: 440px;
    border-radius: 26px; overflow: hidden;
    box-shadow: 0 10px 28px rgba(0,0,0,0.18);
  }

  /* Front: black with faint pattern */
  .card-front { background: var(--ink); color: var(--light-text); }
  .card-front .pattern {
    position: absolute; inset: 0;
    background: radial-gradient(ellipse at 50% 45%, #262323 0%, var(--ink-soft) 55%, var(--ink) 100%);
  }
  .brand {
    position: absolute; left: 0; right: 0;
    display: flex; align-items: center; justify-content: center; gap: 14px;
    font-weight: 500; letter-spacing: 0.06em; text-transform: uppercase;
  }
  .brand .mark {
    width: 30px; height: 30px; border-radius: 50%; background: var(--red);
  }
  .card-front .brand { top: 168px; font-size: 34px; color: var(--light-text); }
  .card-front .web {
    position: absolute; left: 0; right: 0; top: 330px;
    text-align: center; font-size: 20px; letter-spacing: 0.03em; color: var(--light-text);
  }

  /* Back: white with red swoosh and black band */
  .card-back { background: var(--paper); }
  .card-back .bands { position: absolute; inset: 0; }
  .card-back .brand { top: 100px; font-size: 28px; color: var(--ink); }
  .contact {
    position: absolute; color: var(--light-text);
    font-size: 20px; line-height: 26px; letter-spacing: 0.02em; white-space: nowrap;
  }
  .contact .icon { width: 18px; height: 18px; vertical-align: -2px; margin-right: 10px; }
  .phone { left: 58px; top: 296px; }
  .person { left: 330px; top: 292px; }
  .person .name { color: var(--red); font-weight: 600; font-size: 22px; }
  .person .role { margin-left: 10px; font-size: 20px; color: var(--light-text); }
  .email { left: 330px; top: 334px; }
  .site { left: 330px; top: 372px; }
</style>
</head>
<body>
<main class="sheet">

  <section class="card card-front" aria-label="Card front">
    <div class="pattern" role="img" aria-label="Faint repeating star pattern across a black background"></div>
    <div class="brand"><span class="mark"></span><span class="brand-name">K&amp;R Talent Collective</span></div>
    <p class="web">www.krtalentcollective.example</p>
  </section>

  <section class="card card-back" aria-label="Card back">
    <svg class="bands" viewBox="0 0 770 440" preserveAspectRatio="none" aria-hidden="true">
      <path d="M0,140 C200,230 450,268 770,272 L770,276 C450,282 200,262 0,200 Z" fill="var(--red)"/>
      <path d="M0,200 C200,262 450,282 770,276 L770,440 L0,440 Z" fill="var(--ink)"/>
    </svg>

    <div class="brand"><span class="mark"></span><span class="brand-name">K&amp;R Talent Collective</span></div>

    <p class="contact phone">
      <svg class="icon" viewBox="0 0 24 24" aria-hidden="true"><path fill="currentColor" d="M6.6 10.8a15 15 0 0 0 6.6 6.6l2.2-2.2c.3-.3.7-.4 1-.2 1.1.4 2.3.6 3.6.6.6 0 1 .4 1 1V20c0 .6-.4 1-1 1A17 17 0 0 1 3 4c0-.6.4-1 1-1h3.5c.6 0 1 .4 1 1 0 1.3.2 2.5.6 3.6.1.3 0 .7-.2 1z"/></svg>555-804-2917
    </p>
    <p class="contact person"><span class="name">Dorian T. Vickers</span><span class="role">C.E.O</span></p>
    <p class="contact email">
      <svg class="icon" viewBox="0 0 24 24" aria-hidden="true"><rect x="2" y="5" width="20" height="14" rx="1.5" fill="none" stroke="currentColor" stroke-width="2"/><path d="M3 6l9 7 9-7" fill="none" stroke="currentColor" stroke-width="2"/></svg>dtvickers@krtalentcollective.example
    </p>
    <p class="contact site">
      <svg class="icon" viewBox="0 0 24 24" aria-hidden="true"><g fill="none" stroke="currentColor" stroke-width="1.8"><circle cx="12" cy="12" r="9.5"/><ellipse cx="12" cy="12" rx="4.2" ry="9.5"/><path d="M2.5 12h19M4 7h16M4 17h16"/></g></svg>www.krtalentcollective.example
    </p>
  </section>

</main>
</body>
</html>
```